Tender Lantern Letterhead Design Project

We need a letterhead design for a consultancy business based in Australia.

Tender Lantern is a unique business designed to assist with the complex and time consuming nature of selecting contractors, showing them what to do and reviewing quotes when it comes to body corporate and strata maintenance items such as painting, waterproofing, plumbing and electrical.

Target Market(s)

apartment managers

Industry/Entity Type

Business

Requirements
Must have
• must have logo and contact details

Tender Lantern
82 Corvalla Ridge Road
Tarrowin, QLD 4871
Ph 07 5391 2846
Fax 07 5392 8071
Mobile 0438 917204

```html
<!DOCTYPE html>
<html lang="en">
<head>
<meta charset="utf-8">
<title>Tender Lantern Letterhead</title>
<link href="https://fonts.googleapis.com/css2?family=Fira+Sans:wght@400;500&display=swap" rel="stylesheet">
<style>
  :root {
    --backdrop: #2b2b2b;
    --paper: #ffffff;
    --ink: #222222;
    --logo-grey: #9a9a9a;
    --leaf-green: #8dc63f;
    --accent-red: #e31c25;
    --band-orange: #f7941d;
    --rule-grey: #c8c8c8;
    --muted: #7a7a7a;
    --sig-fill: #e6e6e6;
  }
  * { margin: 0; padding: 0; box-sizing: border-box; }
  html, body { width: 1200px; height: 900px; overflow: hidden; background: var(--backdrop); }
  body { font-family: "Fira Sans", sans-serif; position: relative; }

  .letterhead {
    position: absolute; left: 294px; top: 54px;
    width: 612px; height: 791px;
    background: var(--paper); overflow: hidden;
  }
  .brand-name {
    position: absolute; left: 38px; top: 38px;
    font-size: 32px; font-weight: 500; color: var(--logo-grey);
    letter-spacing: -0.5px; line-height: 1;
  }
  .letter-body {
    position: absolute; left: 79px; top: 163px; width: 449px;
    font-size: 9.6px; line-height: 10.2px; color: var(--ink);
    text-align: justify; hyphens: auto;
  }
  .letter-body p { margin-bottom: 10.2px; }
  .signature {
    position: absolute; left: 86px; top: 566px;
    width: 104px; height: 62px; background: var(--sig-fill); border-radius: 4px;
  }
  .rule {
    position: absolute; left: 0; top: 769px; width: 100%; height: 3px;
    background: var(--rule-grey);
  }
  .band {
    position: absolute; left: 0; top: 775px; width: 100%; height: 16px;
    background: var(--band-orange);
  }
  .contact-disc {
    position: absolute; left: 438px; top: 640px;
    width: 196px; height: 196px; border-radius: 50%;
    background: var(--paper); border: 18px solid var(--accent-red);
  }
  .contact {
    position: absolute; left: 476px; top: 679px;
    font-size: 8.6px; line-height: 11px; color: var(--muted);
  }
  .contact .contact-name { color: var(--leaf-green); }
  .contact .lines { margin-bottom: 9px; }
  .contact li { list-style: none; display: flex; align-items: center; gap: 4px; }
  .contact svg { width: 7px; height: 7px; fill: var(--leaf-green); }
</style>
</head>
<body>
  <main class="letterhead">
    <div class="brand-name">Tender Lantern</div>

    <section class="letter-body">
      <p>Lorem ipsum dolor sit amet, consectetuer adipiscing elit. Pellentesque tristique elementum sem. Quisque eget erat ac lectus sodales faucibus. Nam commodo est. Cras consequat faucibus velit. Nam ac magna. Sed et ligula. Nam volutpat, elit ac facilisis tempor, neque augue euismod leo, sit amet molestie sem est eu libero. Nulla facilisi. Pellentesque sit amet odio. Curabitur a leo consectetuer leo blandit porttitor. Pellentesque velit quam, gravida at, pharetra eu, convallis non, sem. Aenean tempor nibh at purus. Pellentesque porta. Suspendisse congue, lacus sit amet imperdiet imperdiet, urna massa rutrum urna, id elementum tellus diam quis risus.</p>
      <p>In dui turpis, varius vitae, tincidunt id, consequat ut, leo. Donec tincidunt tristique odio. Nulla erat felis, euismod nec, fringilla non, aliquet et, magna. Nulla at magna quis nisi pretium vehicula. Pellentesque habitant morbi tristique senectus et netus et malesuada fames ac turpis egestas. Class aptent taciti sociosqu ad litora torquent per conubia nostra, per inceptos himenaeos. In vel quam. Phasellus varius convallis purus. In non turpis. Nam sed risus. Etiam non neque at nisi gravida porttitor. Donec leo dolor, feugiat ut, pharetra et, porttitor a, metus. Suspendisse laoreet magna vel elit. Ut est augue, fermentum ac, molestie at, vestibulum et, urna.</p>
      <p>Nunc purus. Cras auctor. In ornare neque id ipsum. Nulla tincidunt, diam sit amet viverra euismod, sapien augue fringilla neque, at pellentesque felis tortor vel enim. Etiam dignissim. Sed a tortor vel nisl euismod ultricies. Donec molestie congue lectus. Integer sed turpis a tortor imperdiet consequat. Maecenas molestie placerat urna. Sed pede enim, sollicitudin nec, pretium nec, sollicitudin a, felis. In hac habitasse platea dictumst. Nam facilisis, tellus non scelerisque placerat, turpis turpis semper ante, euismod imperdiet augue nisi et neque. Vivamus tincidunt.</p>
      <p>Nulla lobortis ultricies nulla. Pellentesque purus mi, consequat quis, hendrerit sed, imperdiet non, eros. Nullam urna est, vehicula nec, cursus nec, dignissim sit amet, risus. Duis molestie, tellus sit amet laoreet ullamcorper, urna nisi fringilla ante, at rhoncus justo dolor vel dui. Nam hendrerit luctus lorem. Aenean tempor, metus vel posuere gravida, arcu nunc imperdiet tellus, ut blandit sem magna a turpis. Vivamus in neque. Lorem ipsum dolor sit amet, consectetuer adipiscing elit. Duis tristique tortor id nisl feugiat posuere. Maecenas posuere nisi ac risus. Nunc hendrerit. Praesent porta tempus ligula. Morbi in leo. Curabitur sapien nulla, cursus eget, faucibus in, porttitor et, odio. Praesent sed justo sed arcu commodo feugiat. Duis facilisis nulla ut eros. Cras libero. Donec mollis consectetuer metus. Praesent odio.</p>
    </section>

    <div class="signature" role="img" aria-label="Handwritten signature"></div>

    <div class="rule"></div>
    <div class="band"></div>
    <div class="contact-disc"></div>

    <address class="contact" style="font-style:normal">
      <div class="lines">
        <div class="contact-name">Tender Lantern</div>
        <div>82 Corvalla Ridge Road</div>
        <div>Tarrowin, QLD 4871</div>
      </div>
      <ul>
        <li><svg viewBox="0 0 10 10" aria-hidden="true"><path d="M1 3c0-1 1-2 4-2s4 1 4 2v1H7V3H3v1H1z M2 5h6l1 4H1z"/></svg>07 5391 2846</li>
        <li><svg viewBox="0 0 10 10" aria-hidden="true"><path d="M2 1h5v3H2z M1 4h8v5H1z"/></svg>07 5392 8071</li>
        <li><svg viewBox="0 0 10 10" aria-hidden="true"><path d="M1 7h2v2H1z M4 5h2v4H4z M7 2h2v7H7z"/></svg>0438 917204</li>
      </ul>
    </address>
  </main>
</body>
</html>
```